Redesign a product detail page

Our current detail page has to be redesigned. The trouble is, did on a small screen (13 "for example) the drop down menu-are not visible. So the goal is to organize the content i seeking a way, so the 8 drop down menues are visible without scrolling. Please make your . We are looking forward suggestion to see it Here is the currnet page:. https://rauchrohr-versand.de/valdoro-kx-lino/edelstahlkamin-doppelwandig-kx-lino-150mm/ update: I was talking about the 10 -11 drop down menues at the lower side of the product page All which is overwritten with "configuration". See the attached picture. The information in the yellow marker frame shoulderstand be reorganized so it is visible on a 13 "1366x786 screen.

```html
<!DOCTYPE html>
<html lang="de">
<head>
<meta charset="utf-8">
<title>Edelstahlschornstein doppelwandig Ø 150 mm Bausatz – Valdoro KX-LINO</title>
<link rel="stylesheet" href="https://fonts.googleapis.com/css2?family=Open+Sans:wght@400;600;700&display=swap">
<style>
:root{
  --ink:#2b2b2b;
  --muted:#8a8a8a;
  --label:#9a9a9a;
  --line:#d6d6d6;
  --accent:#f7ae2f;
  --accent-soft:#f2ad4f;
  --topbar:#28323d;
  --header:#f6f7f9;
  --search:#b7b7b7;
  --sale:#e8542a;
  --white:#ffffff;
  --media-top:#f5f5f3;
  --media-bottom:#e7e7e3;
}
*{box-sizing:border-box;margin:0;padding:0}
html,body{width:1200px;height:675px;overflow:hidden;background:var(--white);
  font-family:"Open Sans",Arial,sans-serif;color:var(--ink)}
.page{position:relative;width:1200px;height:675px}
.abs{position:absolute}

/* top usp bar */
.usp-bar{left:0;top:0;width:1200px;height:32px;background:var(--topbar);
  display:flex;justify-content:space-between;align-items:center;padding:0 100px 0 99px;
  color:var(--accent);font-size:13px;font-weight:600}

/* header */
.header{left:0;top:32px;width:1200px;height:65px;background:var(--header);border-bottom:1px solid #e3e5e8}
.brand{left:101px;top:46px;display:flex;align-items:center;gap:8px}
.brand-dot{width:38px;height:38px;border-radius:50%;background:var(--accent)}
.brand-name{font-size:16px;font-weight:700;line-height:17px;color:#3a3a3a;letter-spacing:.3px}
.search{left:362px;top:47px;width:255px;height:36px;border-radius:18px;background:var(--search);
  color:#eaeaea;font-size:13px;display:flex;align-items:center;justify-content:center}
.search-btn{left:628px;top:47px;width:37px;height:37px;border-radius:50%;background:var(--accent);
  display:flex;align-items:center;justify-content:center}
.rating-seal{left:863px;top:43px;width:46px;height:46px;border-radius:50%;background:#2d2d2d;border:3px solid #d9d9d9}
.account{left:926px;top:58px;font-size:9.5px;color:var(--muted);display:flex;align-items:center;gap:8px}
.cart{left:1020px;top:52px;font-size:9.5px;color:var(--muted);display:flex;align-items:center;gap:6px}
.cart-count{position:absolute;left:64px;top:-5px;width:13px;height:13px;border-radius:50%;background:var(--accent);
  color:#fff;font-size:8px;text-align:center;line-height:13px}

/* nav */
.nav{left:0;top:97px;width:1200px;height:46px;background:var(--header);border-bottom:1px solid #e3e5e8}
.nav-item{top:110px;font-size:15px;font-weight:600;display:flex;align-items:center;gap:10px}
.phone{left:925px;top:103px;text-align:right;width:174px}
.phone-num{font-size:16px;font-weight:600;letter-spacing:.6px;display:flex;align-items:center;justify-content:flex-end;gap:8px}
.phone-hours{font-size:9.5px;margin-top:2px}

/* breadcrumb */
.breadcrumb{left:99px;top:162px;font-size:11px;color:var(--accent-soft);display:flex;gap:14px}

/* gallery */
.gallery-main{left:99px;top:199px;width:332px;height:371px;border:1px solid #e4e4e4;
  background:linear-gradient(180deg,var(--media-top),var(--media-bottom))}
.free-ship{left:95px;top:217px;width:170px;height:55px;background:var(--accent);color:#fff;
  font-size:12px;font-weight:700;display:flex;align-items:center;gap:9px;padding-left:13px;white-space:nowrap}
.thumbs{left:99px;top:596px;display:flex;gap:15px}
.thumb{width:55px;height:59px;border:1px solid #e1e1e1;padding:3px}
.thumb span{display:block;width:100%;height:100%}

/* tabs */
.tab{top:197px;font-size:11.5px;font-weight:600;letter-spacing:.3px;padding-bottom:4px}
.tab.active{border-bottom:1px solid var(--ink)}

/* configuration */
.config{left:448px;top:253px;display:grid;grid-template-columns:318px 318px;column-gap:17px;row-gap:7px}
.field-label{font-size:11px;color:var(--label);letter-spacing:.2px;margin-bottom:4px;white-space:nowrap}
.select{height:37px;border:1px solid var(--line);display:flex;align-items:center;justify-content:space-between;
  padding:0 14px 0 16px;font-size:8.5px;color:#222}
.help{width:19px;height:19px;border-radius:50%;background:var(--accent);color:#fff;font-size:11px;font-weight:700;
  display:flex;align-items:center;justify-content:center}

/* buy box */
.buy-brand{left:448px;top:610px;display:flex;align-items:center;gap:7px}
.buy-brand .brand-dot{width:27px;height:27px}
.buy-brand .brand-name{font-size:12px;line-height:13px}
.trust-list{left:582px;top:570px;list-style:none;font-size:11px}
.trust-list li{display:flex;align-items:center;gap:10px;height:24.5px}
.trust-list svg{width:15px;height:15px}
.choice-title{left:783px;top:568px;font-size:13px;font-weight:600;letter-spacing:.3px}
.old-price{left:783px;top:595px;font-size:12.5px;color:var(--sale);text-decoration:line-through}
.price{left:783px;top:610px;font-size:21px;font-weight:700}
.price-note{left:785px;top:638px;font-size:7px;line-height:8px;color:#444}
.price-note span{text-decoration:underline}
.qty{left:922px;top:612px;width:37px;height:24px;background:#eee;border:1px solid #ddd;font-size:9px;
  display:flex;align-items:center;justify-content:center;gap:5px}
.add-to-cart{left:993px;top:611px;width:108px;height:24px;border-radius:12px;background:var(--accent);color:#fff;
  font-size:8.5px;font-weight:600;display:flex;align-items:center;justify-content:center;gap:7px}

/* floating rating widget */
.rating-widget{left:1119px;top:309px;width:81px;height:143px;background:#f3f3f3;border:1px solid #dcdcdc;
  text-align:center;border-right:none}
.rating-widget .seal{width:60px;height:60px;border-radius:50%;background:#2d2d2d;border:3px solid #d9d9d9;margin:9px auto 6px}
.rating-widget .cap{font-size:8px;color:#555}
.stars{color:var(--accent);font-size:13px;letter-spacing:-1px;line-height:14px}
.verdict{font-size:13px;font-weight:700;color:#444;line-height:16px}
.score{font-size:11px;color:#555}
.score b{font-weight:700}
</style>
</head>
<body>
<div class="page">

  <div class="abs usp-bar">
    <span>Deutsche Markenqualität</span><span>25 Jahre Garantie</span><span>Schnelle Lieferung</span>
    <span>Kostenlose Fachberatung</span><span>Bundesweiter Montageservice</span>
  </div>

  <div class="abs header"></div>
  <div class="abs brand"><span class="brand-dot"></span><span class="brand-name">RAUCHROHR<br>VERSAND</span></div>
  <div class="abs search">Suchbegriff oder Artikelnummer:</div>
  <div class="abs search-btn">
    <svg width="17" height="17" viewBox="0 0 20 20"><circle cx="8" cy="8" r="6" fill="none" stroke="#fff" stroke-width="2.6"/><path d="M12.5 12.5l5 5" stroke="#fff" stroke-width="2.8" stroke-linecap="round"/></svg>
  </div>
  <div class="abs rating-seal" role="img" aria-label="Kaufsiegel"></div>
  <div class="abs account">Mein Konto
    <svg width="28" height="28" viewBox="0 0 28 28"><circle cx="14" cy="8" r="6.5" fill="#aaa"/><path d="M2 28c0-9 5-13 12-13s12 4 12 13z" fill="#aaa"/></svg>
  </div>
  <div class="abs cart">Warenkorb
    <svg width="28" height="24" viewBox="0 0 28 24"><path d="M2 8h24l-3 15H5z" fill="none" stroke="#aaa" stroke-width="2"/><path d="M8 8l4-6M20 8l-4-6M9 12v7M14 12v7M19 12v7" stroke="#aaa" stroke-width="1.6"/></svg>
    <span class="cart-count">0</span>
  </div>

  <div class="abs nav"></div>
  <div class="abs nav-item" style="left:114px">Online-Shop
    <svg width="10" height="6" viewBox="0 0 10 6"><path d="M1 1l4 4 4-4" fill="none" stroke="#777" stroke-width="1.3"/></svg></div>
  <div class="abs nav-item" style="left:252px">Service
    <svg width="10" height="6" viewBox="0 0 10 6"><path d="M1 1l4 4 4-4" fill="none" stroke="#777" stroke-width="1.3"/></svg></div>
  <div class="abs phone">
    <div class="phone-num">
      <svg width="18" height="18" viewBox="0 0 20 20"><path d="M4 2l4 1 1 4-2 2c1 2 3 4 5 5l2-2 4 1 1 4-3 2C9 19 1 11 2 5z" fill="#222"/></svg>
      0800 / 724 318 0</div>
    <div class="phone-hours">Mo. - Fr. von 09:00 bis 18:00 Uhr</div>
  </div>

  <nav class="abs breadcrumb">
    <span>Rauchrohr-Versand</span><span>&gt;</span><span>Valdoro KX-LINO</span><span>&gt;</span>
    <span>Edelstahlschornstein doppelwandig Ø 150 mm Bausatz - Valdoro KX-LINO</span>
  </nav>

  <div class="abs gallery-main" role="img" aria-label="Produktdarstellung: doppelwandiger Edelstahlschornstein an einer Hauswand montiert"></div>
  <div class="abs free-ship">
    <svg width="28" height="24" viewBox="0 0 28 24"><path d="M2 9h24l-3 14H5z" fill="none" stroke="#fff" stroke-width="2"/><path d="M8 9l4-7M20 9l-4-7M9 13v6M14 13v6M19 13v6" stroke="#fff" stroke-width="1.6"/></svg>
    Versandkostenfrei</div>
  <div class="abs thumbs">
    <div class="thumb"><span role="img" aria-label="Produktfoto Fassade" style="background:linear-gradient(90deg,#8f98ad,#c9b27a)"></span></div>
    <div class="thumb"><span role="img" aria-label="Produktfoto Montage" style="background:linear-gradient(90deg,#aab4c8,#e6e9ef)"></span></div>
    <div class="thumb"><span role="img" aria-label="Produktfoto Wandhalterung" style="background:linear-gradient(90deg,#c8b070,#9aa6b8)"></span></div>
    <div class="thumb"><span role="img" aria-label="Technische Ansicht Bausatz" style="background:#f2f2f2"></span></div>
    <div class="thumb"><span role="img" aria-label="Technische Ansicht Bausatz" style="background:#f2f2f2"></span></div>
  </div>

  <div class="abs tab" style="left:449px">DESCRIPTION</div>
  <div class="abs tab active" style="left:548px">KONFIGURATION</div>

  <div class="abs config">
    <div><div class="field-label">HÖHE DES SCHORNSTEINS WÄHLEN: *</div><div class="select">--- Please Select ---<span class="help">?</span></div></div>
    <div><div class="field-label">HÖHE DES SCHORNSTEINS WÄHLEN: *</div><div class="select">--- Please Select ---<span class="help">?</span></div></div>
    <div><div class="field-label">MONTAGEART WÄHLEN: *</div><div class="select">--- Please Select ---<span class="help">?</span></div></div>
    <div><div class="field-label">MONTAGEART WÄHLEN: *</div><div class="select">--- Please Select ---<span class="help">?</span></div></div>
    <div><div class="field-label">WANDABSTAND WÄHLEN: *</div><div class="select">--- Please Select ---<span class="help">?</span></div></div>
    <div><div class="field-label">WANDABSTAND WÄHLEN: *</div><div class="select">--- Please Select ---<span class="help">?</span></div></div>
    <div><div class="field-label">ZWEITE REINIGUNGSÖFFNUNG / PRÜFÖFFNUNG WÄHLEN:</div><div class="select">--- Please Select ---<span class="help">?</span></div></div>
    <div><div class="field-label">ZWEITE REINIGUNGSÖFFNUNG / PRÜFÖFFNUNG WÄHLEN:</div><div class="select">--- Please Select ---<span class="help">?</span></div></div>
    <div><div class="field-label">BITTE ANSCHLUSSDURCHMESSER ANGEBEN:</div><div class="select">--- Please Select ---<span class="help">?</span></div></div>
    <div><div class="field-label">BITTE ANSCHLUSSDURCHMESSER ANGEBEN:</div><div class="select">--- Please Select ---<span class="help">?</span></div></div>
  </div>

  <div class="abs buy-brand"><span class="brand-dot"></span><span class="brand-name">RAUCHROHR<br>VERSAND</span></div>
  <ul class="abs trust-list">
    <li><svg viewBox="0 0 16 16"><circle cx="8" cy="8" r="7" fill="none" stroke="#333" stroke-width="1.3"/><circle cx="5.5" cy="6.3" r="1" fill="#333"/><circle cx="10.5" cy="6.3" r="1" fill="#333"/><path d="M4.5 9.5c1.5 2.2 5.5 2.2 7 0" fill="none" stroke="#333" stroke-width="1.3"/></svg>Über 10000 zufriedene Kunden</li>
    <li><svg viewBox="0 0 16 16"><rect x="3" y="7" width="10" height="8" fill="#333"/><path d="M5 7V5a3 3 0 016 0v2" fill="none" stroke="#333" stroke-width="1.6"/></svg>Sichere Bestellabwicklung</li>
    <li><svg viewBox="0 0 16 16"><circle cx="8" cy="6" r="4.8" fill="#333"/><path d="M5 10l-2 5 3-1 1 2 1-5M11 10l2 5-3-1-1 2-1-5" fill="#333"/></svg>25 Jahre Garantie</li>
    <li><svg viewBox="0 0 16 16"><path d="M1 4h9v7H1zM10 6h3l2 3v2h-5z" fill="#333"/><circle cx="4" cy="12" r="1.7" fill="#333"/><circle cx="12" cy="12" r="1.7" fill="#333"/></svg>Sofort versandbereit</li>
  </ul>
  <div class="abs choice-title">Ihre Auswahl</div>
  <div class="abs old-price">€ 750,99</div>
  <div class="abs price">€ 560,07</div>
  <div class="abs price-note">Preise inkl. gesetzlicher USt.<br><span>zzgl. Versand (in D max. € 5,90)</span></div>
  <div class="abs qty">1
    <svg width="7" height="5" viewBox="0 0 10 6"><path d="M1 1l4 4 4-4" fill="none" stroke="#777" stroke-width="1.4"/></svg></div>
  <div class="abs add-to-cart">In den Warenkorb
    <svg width="5" height="8" viewBox="0 0 6 10"><path d="M1 1l4 4-4 4" fill="none" stroke="#fff" stroke-width="1.6"/></svg></div>

  <aside class="abs rating-widget">
    <div class="seal" role="img" aria-label="Kaufsiegel"></div>
    <div class="cap">Kundenbewertung</div>
    <div class="stars">★★★★★</div>
    <div class="verdict">SEHR GUT</div>
    <div class="score"><b>4.66</b>/5.00</div>
  </aside>

</div>
</body>
</html>
```